VARDEN INSULATION STATIONARY
BUSINESS CARDS,STATIONARY,ENVELOPES & T-SHIRTS
Modern
ED VARDEN
OWNER,SALES
14 BRISTLECONE CT. FERNHOLLOW, ST 00417
VARDENINSULATION@MAILNEST.EXAMPLE
WWW.VARDENINSULATION.EXAMPLE
I'M GOING TO GET A WEBSITE DESIGN HERE TOO,THATS WHY I'M USING THE WEBSITE ADDRESS,PROBABLY MY E-MAIL IS GOING TO CHANGE AFTER I GET THE WEBSITE,BUT I THINK THIS IS EASY TO CHANGE.

```html
<!DOCTYPE html>
<html lang="en">
<head>
<meta charset="utf-8">
<title>Varden Insulation Stationery</title>
<link rel="stylesheet" href="https://fonts.googleapis.com/css2?family=Montserrat:wght@700&family=Open+Sans:wght@400;700&display=swap">
<style>
  :root {
    --green-dark: #1a7a35;
    --green-mid: #2f9a3e;
    --green-light: #8cc63f;
    --paper: #ffffff;
    --bg: #ffffff;
    --ink: #333333;
    --ghost: #f2f4f2;
  }
  * { margin: 0; padding: 0; box-sizing: border-box; }
  html, body { width: 1200px; height: 1101px; overflow: hidden; background: var(--bg); }
  body { position: relative; font-family: "Open Sans", Arial, sans-serif; color: var(--ink); }
  address { font-style: normal; }

  .sheet { position: absolute; background: var(--paper); box-shadow: 0 1px 4px rgba(0,0,0,.25); overflow: hidden; }

  .brand { display: flex; align-items: center; gap: 10px; font-family: "Montserrat", Arial, sans-serif; font-weight: 700; color: var(--green-dark); line-height: 1.05; }
  .brand-mark { background: var(--green-dark); flex: none; }

  /* Letterhead */
  .letterhead { left: 15px; top: 15px; width: 840px; height: 1071px; }
  .letterhead .brand { position: absolute; left: 470px; top: 95px; font-size: 28px; }
  .letterhead .brand-mark { width: 44px; height: 44px; }
  .ghost-decoration { position: absolute; left: 190px; top: 420px; width: 260px; height: 420px; background: linear-gradient(160deg, #f5f6f5, var(--ghost)); }
  .wave { position: absolute; left: 0; bottom: 0; width: 100%; }
  .letterhead .wave { height: 240px; }
  .letter-contact { position: absolute; left: 30px; bottom: 34px; color: #fff; font-size: 14px; line-height: 1.45; }
  .site { position: absolute; display: flex; align-items: center; gap: 6px; color: var(--green-dark); font-size: 14px; white-space: nowrap; }
  .site-dot { width: 10px; height: 10px; background: var(--green-light); flex: none; }
  .letterhead .site { left: 500px; top: 912px; font-size: 13px; }

  /* Envelope */
  .envelope-flap { position: absolute; left: 405px; top: 405px; width: 780px; height: 92px; }
  .flap-site { position: absolute; left: 715px; top: 446px; width: 170px; text-align: center; color: #fff; font-size: 11px; transform: rotate(180deg); }
  .envelope { left: 405px; top: 495px; width: 780px; height: 430px; }
  .envelope .brand { position: absolute; right: 40px; top: 105px; font-size: 30px; }
  .envelope .brand-mark { width: 46px; height: 46px; }
  .envelope .site { right: 40px; top: 200px; font-size: 13px; }
  .envelope .wave { height: 230px; }
  .envelope-contact { position: absolute; left: 30px; top: 262px; font-size: 12.5px; line-height: 1.45; color: #fff; }

  /* Business card */
  .card-front { left: 900px; top: 30px; width: 285px; height: 156px; }
  .card-front .brand { position: absolute; left: 14px; top: 16px; font-size: 14px; gap: 6px; }
  .card-front .brand-mark { width: 22px; height: 22px; }
  .card-name { position: absolute; right: 14px; top: 16px; text-align: right; color: var(--green-dark); font-family: "Montserrat", Arial, sans-serif; font-weight: 700; font-size: 16px; }
  .card-role { display: block; font-family: "Open Sans", Arial, sans-serif; font-weight: 400; font-size: 8px; color: var(--ink); }
  .card-address { position: absolute; left: 14px; top: 66px; font-size: 7.5px; line-height: 1.4; }
  .card-phones { position: absolute; left: 160px; top: 66px; font-size: 7.5px; line-height: 1.4; }
  .card-front .wave { height: 50px; }
  .card-back { left: 900px; top: 204px; width: 285px; height: 162px; background: linear-gradient(160deg, var(--green-mid), var(--green-dark)); }
  .card-back .site { left: 70px; top: 74px; color: #fff; font-size: 9px; gap: 4px; }
  .card-back .site-dot { width: 7px; height: 7px; }
</style>
</head>
<body>

<section class="sheet letterhead">
  <div class="ghost-decoration" role="img" aria-label="Faint large brand decoration"></div>
  <div class="brand"><span class="brand-mark"></span><span>VARDEN<br>INSULATION</span></div>
  <svg class="wave" viewBox="0 0 840 240" preserveAspectRatio="none">
    <path d="M0,20 C180,12 330,70 480,118 C600,156 700,172 760,178 L340,240 L0,240Z" fill="var(--green-dark)"/>
    <path d="M380,240 C560,192 700,165 840,150 L840,182 C700,192 570,212 480,240Z" fill="var(--green-light)"/>
    <path d="M480,240 C610,220 720,206 840,198 L840,240Z" fill="var(--green-mid)"/>
  </svg>
  <div class="site"><span class="site-dot"></span>www.vardeninsulation.example</div>
  <address class="letter-contact">
    <b>Address:</b> 14 Bristlecone<br>
    Ct. Fernhollow, ST 00417<br>
    <b>Phone:</b> (555) 010-0148<br>
    <b>Cell:</b> (555) 010-0172 <b>Fax:</b> (555) 010-0149<br>
    vardeninsulation@mailnest.example
  </address>
</section>

<svg class="envelope-flap" viewBox="0 0 780 92" preserveAspectRatio="none">
  <defs>
    <linearGradient id="flapFill" x1="0" y1="0" x2="0" y2="1">
      <stop offset="0" stop-color="#2f9a3e"/><stop offset="1" stop-color="#1a7a35"/>
    </linearGradient>
  </defs>
  <polygon points="0,92 390,0 780,92" fill="url(#flapFill)"/>
</svg>
<div class="flap-site">vardeninsulation.example</div>

<section class="sheet envelope">
  <div class="brand"><span class="brand-mark"></span><span>VARDEN<br>INSULATION</span></div>
  <div class="site"><span class="site-dot"></span>www.vardeninsulation.example</div>
  <svg class="wave" viewBox="0 0 780 230" preserveAspectRatio="none">
    <path d="M0,20 C200,10 380,70 520,115 C620,145 680,158 720,162 L300,230 L0,230Z" fill="var(--green-dark)"/>
    <path d="M340,230 C510,185 650,160 780,148 L780,178 C650,188 530,208 440,230Z" fill="var(--green-light)"/>
    <path d="M440,230 C570,212 680,200 780,195 L780,230Z" fill="var(--green-mid)"/>
  </svg>
  <address class="envelope-contact">
    <b>Address:</b><br>
    14 Bristlecone Ct. Fernhollow, ST 00417<br>
    <b>Phone:</b> (555) 010-0148 <b>Cell:</b> (555) 010-0172<br>
    <b>Fax:</b> (555) 010-0149<br>
    vardeninsulation@mailnest.example
  </address>
</section>

<section class="sheet card-front">
  <div class="brand"><span class="brand-mark"></span><span>VARDEN<br>INSULATION</span></div>
  <div class="card-name">ED VARDEN<span class="card-role">Owner, Sales</span></div>
  <address class="card-address">
    <b>Address:</b><br>14 Bristlecone Ct.<br>Fernhollow, ST 00417<br>vardeninsulation@mailnest.example
  </address>
  <div class="card-phones">
    Phone: (555) 010-0148<br>Cell: (555) 010-0172<br>Fax: (555) 010-0149
  </div>
  <svg class="wave" viewBox="0 0 285 50" preserveAspectRatio="none">
    <path d="M0,20 C90,12 170,40 285,34 L285,50 L0,50Z" fill="var(--green-dark)"/>
    <path d="M130,50 C190,40 240,36 285,38 L285,50Z" fill="var(--green-light)"/>
  </svg>
</section>

<section class="sheet card-back">
  <div class="site"><span class="site-dot"></span>www.vardeninsulation.example</div>
</section>

</body>
</html>
```